Bluestone Auto Works | ||
Bluestone | ||
Automotive | ||
Bluestone Auto Works is a auto reseller, that offers consignment, brokerage, and restoration services. | ||
Like black back grounds, dislike hookey websites | ||
Cutting-Edge Professional Trendy Sophisticated Modern Elegant Progressive Service Oriented High Tech Masculine |
black backgroung | ||
left side | ||
www.dravelkustom.com | ||
http://www.harborlinebuilds.com/ | ||
http://www.ridgefieldcycleworks.com/ | ||
used logo to coordinate colors | ||

```html
<!DOCTYPE html>
<html lang="en">
<head>
<meta charset="utf-8">
<title>Bluestone Auto Works</title>
<link href="https://fonts.googleapis.com/css2?family=Arimo:wght@400;700&display=swap" rel="stylesheet">
<style>
:root{
  --bg:#141414;
  --bg-light:#262626;
  --panel:#1d1d1d;
  --panel-edge:#333;
  --orange:#f26a10;
  --orange-light:#ff9a3c;
  --orange-dark:#c94a00;
  --text:#e6e6e6;
  --muted:#b4b4b4;
  --white:#fff;
}
*{margin:0;padding:0;box-sizing:border-box}
html,body{width:1200px;height:1033px;overflow:hidden}
body{
  position:relative;
  font-family:"Arimo",Arial,sans-serif;
  color:var(--text);
  background:radial-gradient(ellipse at 50% 30%,var(--bg-light),var(--bg) 70%);
}
.top-band{position:absolute;left:0;top:0;width:1200px;height:70px}
.logo{position:absolute;left:175px;top:38px;display:flex;align-items:center;gap:10px;
  font-size:28px;font-weight:700;color:var(--white)}
.logo .mark{width:26px;height:26px;border-radius:50%;background:var(--orange)}
.nav{position:absolute;right:176px;top:74px;display:flex;font-size:15px}
.nav a{color:var(--white);text-decoration:none;padding:0 13px;border-left:1px solid #666;line-height:14px}
.nav a:first-child{border-left:none;color:var(--orange)}
.hero{position:absolute;left:173px;top:106px;width:851px;height:290px;
  background:linear-gradient(180deg,#7e8380 0%,#8a4a36 45%,#a8361a 60%,#2e2f2e 100%);border:2px solid #3a3a3a}
.arrow{position:absolute;top:240px;width:0;height:0;border-top:12px solid transparent;border-bottom:12px solid transparent}
.arrow.prev{left:182px;border-right:14px solid #ddd}
.arrow.next{left:1002px;border-left:14px solid #ddd}
.heading{position:absolute;font-size:21px;color:var(--white);padding-bottom:4px;border-bottom:2px solid var(--orange)}
.models-list{position:absolute;left:173px;top:446px;width:184px;height:280px;
  background:linear-gradient(90deg,var(--orange-dark),var(--orange) 60%,var(--orange-light));list-style:none;padding:6px 0}
.models-list li{font-size:14.5px;color:#1a1a1a;padding:2.6px 0 2.6px 20px;line-height:17px}
.models-list li:first-child{background:rgba(255,255,255,.35)}
.models-list .scroll{position:absolute;right:8px;top:12px;width:7px;height:250px;background:rgba(0,0,0,.25);border-radius:4px}
.models-list .scroll::after{content:"";position:absolute;left:0;top:30px;width:7px;height:70px;background:#2a2a2a;border-radius:4px}
.hours{position:absolute;left:173px;top:767px;width:184px;height:122px;
  background:linear-gradient(135deg,#8d8d8d,#4b4b4b);border:1px solid var(--panel-edge)}
.hours .num{position:absolute;left:16px;top:14px;font-size:60px;line-height:70px;color:#1c1c1c}
.hours .label{position:absolute;left:18px;top:92px;font-size:13px;color:#1c1c1c}
.hours svg{position:absolute;left:112px;top:22px}
.panel{position:absolute;left:377px;width:647px;background:var(--panel);border:1px solid var(--panel-edge)}
.panel p{position:absolute;font-size:12px;line-height:17px;color:var(--muted)}
.thumb{position:absolute;background:linear-gradient(135deg,#6a1420,#2a0a0e 70%,#555)}
.more{position:absolute;width:76px;height:20px;background:var(--orange);color:#1a1a1a;font-size:13px;
  line-height:20px;padding-left:14px}
.footer-line{position:absolute;left:0;top:940px;width:1200px;height:5px;background:var(--orange)}
footer{position:absolute;left:0;top:945px;width:1200px;height:88px;background:linear-gradient(180deg,#303030,#121212)}
.foot-logo{position:absolute;left:186px;top:30px;font-size:24px;font-weight:700;color:#6a6a6a}
.follow{position:absolute;left:517px;top:35px;display:flex;align-items:center;gap:8px;font-size:15px;color:var(--white)}
.follow span.icon{width:26px;height:26px;background:#5a7fb0;display:inline-block}
.follow span.icon:nth-child(3){background:#38a8e0}
.follow span.icon:nth-child(4){background:#c0302a}
.copy{position:absolute;right:176px;top:40px;font-size:13px;color:var(--muted)}
</style>
</head>
<body>
<svg class="top-band" viewBox="0 0 1200 70" aria-hidden="true">
  <polygon points="700,0 1200,0 1200,30 990,30 960,10 720,10" fill="#0c0c0c"/>
  <polygon points="960,10 1200,10 1200,70 1060,70" fill="var(--orange)"/>
</svg>

<header>
  <div class="logo"><span class="mark"></span>Bluestone</div>
  <nav class="nav">
    <a href="#">Home</a><a href="#">About us</a><a href="#">Services</a><a href="#">New Cars</a><a href="#">Accessories</a><a href="#">Contact us</a>
  </nav>
</header>

<div class="hero" role="img" aria-label="Red classic coupe parked at a car show"></div>
<span class="arrow prev"></span><span class="arrow next"></span>

<h2 class="heading" style="left:173px;top:410px;width:184px">Models</h2>
<ul class="models-list">
  <li>Alvera Rossi</li><li>Ascoro</li><li>Ashford Marten</li><li>Aurel</li><li>Bentrow</li><li>BKV</li>
  <li>Brovus</li><li>Bugello</li><li>Caterwick</li><li>Corvane</li><li>Ferrano</li><li>Gumhart</li>
  <span class="scroll"></span>
</ul>

<h2 class="heading" style="left:173px;top:733px;width:184px">Our Hours</h2>
<div class="hours">
  <span class="num">24</span>
  <span class="label">Hours Services</span>
  <svg width="56" height="56" viewBox="0 0 60 60" aria-hidden="true">
    <circle cx="30" cy="30" r="27" fill="none" stroke="#222" stroke-width="3"/>
    <line x1="30" y1="30" x2="30" y2="12" stroke="#222" stroke-width="3"/>
    <line x1="30" y1="30" x2="42" y2="36" stroke="#222" stroke-width="3"/>
  </svg>
</div>

<h2 class="heading" style="left:377px;top:410px;width:647px">New Cars</h2>
<div class="panel" style="top:441px;height:134px">
  <div class="thumb" role="img" aria-label="Dark red custom hot rod" style="left:5px;top:6px;width:288px;height:120px"></div>
  <p style="left:305px;top:8px;width:330px">What is the most expensive car in the world? The 1931 Bugello Regal Kellan Coupe was sold for $8,700,000 in 1987. However, that car and many alike will not be included in this list because it is not available on the market today. It is hard to imagine someone would spend 8 million dollars on a car.</p>
  <span class="more" style="right:0;top:113px">more...</span>
</div>

<h2 class="heading" style="left:377px;top:586px;width:647px">Services</h2>
<div class="panel" style="top:618px;height:110px">
  <p style="left:14px;top:10px;width:610px">What is the most expensive car in the world? The 1931 Bugello Regal Kellan Coupe was sold for $8,700,000 in 1987. However, that car and many alike will not be included in this list because it is not available on the market today. It is hard to imagine someone would actually spend 8 million dollars on a car instead of using it for something else</p>
  <span class="more" style="right:0;top:88px">more...</span>
</div>

<h2 class="heading" style="left:377px;top:733px;width:647px">Customer Reviews</h2>
<div class="panel" style="top:770px;height:118px">
  <div class="thumb" role="img" aria-label="Customer's restored car" style="left:5px;top:18px;width:64px;height:64px;background:linear-gradient(135deg,#707a80,#2a2e30)"></div>
  <p style="left:84px;top:18px;width:540px">What is the most expensive car in the world? The 1931 Bugello Regal Kellan Coupe was sold for $8,700,000 in 1987. However, that car and many alike will not be included in this list because it is not available on the market today.</p>
  <span class="more" style="right:0;top:96px">more...</span>
</div>

<div class="footer-line"></div>
<footer>
  <div class="foot-logo">Bluestone</div>
  <div class="follow">Follow us on <span class="icon"></span><span class="icon"></span><span class="icon"></span></div>
  <div class="copy">©2012 Bluestone Auto Works.com</div>
</footer>
</body>
</html>
```